velto GmbH - Business Cards etc.
velto GmbH
Project: velto GmbH - Business Cards etc.
velto GmbH - Business Cards etc. - Retailers
Creative Brief
Professional
Konrad Wieslauer
CEO
Gisela Brandtner Str. 23 76139 Karlsruhe
k.wieslauer@veltohouse.com
www.veltohouse.com
The business card MUST have the following format: 85 x 55mm PLUS a 3mm addition on every side. This means the image size must be 91 x 61mm
Concepts
Business Cards/Letterhead/ Envelopes/Notepads/Tshirt/labels for tiny tall crate
Business cards and company letter head for Osaka Dine Court
konrad konrad
I don't have a logo unfortunately. I've started a logo design project but it was not successful. I really need biz cards now and want to find a logo later. The logo on the biz cards is not so important in this case.
I wonder why there are so few contributions to this project? What's missing? How can I help?

```html
<!DOCTYPE html>
<html lang="de">
<head>
<meta charset="utf-8">
<title>velto GmbH – Visitenkarte</title>
<link href="https://fonts.googleapis.com/css2?family=Roboto:wght@300;400&family=Roboto+Condensed:wght@400&display=swap" rel="stylesheet">
<style>
  :root {
    --page: #ffffff;
    --card: #ffffff;
    --card-edge: #d9d9d9;
    --band-grey: #d4d5d7;
    --accent-red: #e8412c;
    --text-dark: #4a4a4a;
    --text-body: #3c3c3c;
  }
  html, body {
    margin: 0;
    width: 1200px;
    height: 871px;
    overflow: hidden;
    background: var(--page);
    font-family: "Roboto", Arial, sans-serif;
  }
  .card {
    position: absolute;
    left: 368px;
    top: 37px;
    width: 465px;
    height: 800px;
    background: var(--card);
    outline: 1px solid var(--card-edge);
    overflow: hidden;
  }
  .card__side-band {
    position: absolute;
    left: 0;
    top: 0;
    width: 130px;
    height: 100%;
    background: var(--band-grey);
  }
  .card__brand {
    position: absolute;
    left: 262px;
    top: 34px;
    display: flex;
    align-items: center;
    gap: 12px;
  }
  .card__brand-square {
    width: 24px;
    height: 24px;
    background: var(--accent-red);
  }
  .card__brand-name {
    margin: 0;
    font-weight: 300;
    font-size: 26px;
    line-height: 1;
    color: var(--text-dark);
    white-space: nowrap;
  }
  .card__name {
    position: absolute;
    left: 38px;
    top: 366px;
    margin: 0;
    font-weight: 300;
    font-size: 46px;
    line-height: 1;
    color: var(--text-dark);
    white-space: nowrap;
  }
  .card__role {
    position: absolute;
    left: 240px;
    top: 428px;
    margin: 0;
    font-weight: 400;
    font-size: 21px;
    line-height: 1;
    color: var(--text-dark);
  }
  .card__contact {
    position: absolute;
    left: 26px;
    top: 608px;
    margin: 0;
    font-family: "Roboto Condensed", "Arial Narrow", sans-serif;
    font-style: normal;
    font-weight: 400;
    font-size: 21px;
    line-height: 26px;
    color: var(--text-body);
  }
  .card__contact span { display: block; white-space: nowrap; }
</style>
</head>
<body>
  <article class="card">
    <div class="card__side-band"></div>

    <div class="card__brand">
      <span class="card__brand-square"></span>
      <p class="card__brand-name">VELTO GmbH</p>
    </div>

    <h1 class="card__name">Konrad Wieslauer</h1>
    <p class="card__role">CEO</p>

    <address class="card__contact">
      <span>Gisela Brandtner Str. 23</span>
      <span>76139 Lindenfeld Phone +49 (0) 634 482 3061</span>
      <span>Fax +49 (0) 634 482 3062</span>
      <span>Email: k.wieslauer@veltohouse.com</span>
      <span>www.veltohouse.com</span>
    </address>
  </article>
</body>
</html>
```